Brantley Advisory Group provides support for renewable energy projects to utilities and suppliers

I need a professional looking business card that is both simple and elegant and unique. My clients are mostly large organizations not individuals. I am a consultant with my own company that is small but would like to give clients the impression I am larger. Smart grid, fiber optics, software, field hardware, distribution automation, substation automation, operations, energy storage/batteries, microgrids, customer service, strategy/roadmaps, conservation, Automated Metering Infrastruture (AMI or smart meters) are all areas of focus.

Target Market(s)

Utilities, suppliers, governmental agencies involved in energy. All types of energy especially natural gas and electrical. Especially renewable energy or green projects.

Contact Information for Business Card

Name - Mark Brantley Cell Phone - 425.318.2746 Email - mbrantley@brantleyag-example.com
Company - Brantley Advisory Group (logo) Title - Principal

Font styles to use
Serif
Sans Serif

Colors

Designer to choose colors to be used in the design.

Requirements
Must have
• Simple and professional and powerful.
• Unique/creative design.
Nice to have
• Utilize color scheme to accent logo colors. Maybe some geometric pattern on edge of card with color.
Should not have
• Busy, complicated, traditional

```html
<!DOCTYPE html>
<html lang="en">
<head>
<meta charset="UTF-8">
<title>Brantley Advisory Group — Business Card</title>
<link rel="stylesheet" href="https://fonts.googleapis.com/css2?family=Tenor+Sans&display=swap">
<style>
  :root {
    --backdrop: #3c3f46;
    --card: #030303;
    --pattern-dark: #1c1c1c;
    --pattern-mid: #2a2a2a;
    --brand-blue: #3554b8;
    --brand-green: #6a9a3a;
    --text-font: "Tenor Sans", sans-serif;
  }
  html, body {
    margin: 0;
    padding: 0;
    width: 1200px;
    height: 675px;
    overflow: hidden;
    background: var(--backdrop);
    font-family: var(--text-font);
  }
  .stage {
    width: 1200px;
    height: 675px;
    display: flex;
    align-items: center;
    justify-content: center;
    gap: 80px;
  }
  .card {
    position: relative;
    width: 320px;
    height: 560px;
    background: var(--card);
    overflow: hidden;
    box-shadow: 0 12px 30px rgba(0,0,0,0.35);
  }
  .pattern-top,
  .pattern-bottom {
    position: absolute;
    left: 0;
    width: 100%;
  }
  .pattern-top {
    top: 0;
    height: 150px;
    background: linear-gradient(to bottom, var(--pattern-mid), var(--pattern-dark) 45%, var(--card));
  }
  .pattern-bottom {
    bottom: 0;
    height: 170px;
    background: linear-gradient(to top, var(--pattern-mid), var(--pattern-dark) 50%, var(--card));
  }
  .brand {
    position: absolute;
    left: 30px;
    right: 20px;
    display: flex;
    align-items: center;
    gap: 12px;
  }
  .card-front .brand { top: 150px; }
  .card-back .brand { top: 195px; }
  .brand-mark {
    width: 30px;
    height: 30px;
    flex: none;
    border: 2px solid var(--brand-green);
    box-sizing: border-box;
  }
  .brand-name {
    color: var(--brand-blue);
    font-size: 22px;
    line-height: 1.15;
    letter-spacing: 0.5px;
  }
  .contact {
    position: absolute;
    left: 30px;
    right: 24px;
    top: 340px;
  }
  .contact-name {
    color: var(--brand-green);
    font-size: 22px;
    font-variant: small-caps;
    letter-spacing: 1px;
    margin: 0 0 6px;
    font-weight: normal;
  }
  .contact-rule {
    height: 2px;
    background: var(--brand-blue);
    border: 0;
    margin: 0 0 12px;
  }
  .contact-line {
    display: flex;
    align-items: center;
    gap: 10px;
    color: var(--brand-green);
    font-size: 13px;
    margin: 0 0 7px 4px;
    letter-spacing: 0.3px;
  }
  .contact-line svg {
    width: 12px;
    height: 12px;
    flex: none;
    fill: var(--brand-blue);
  }
</style>
</head>
<body>
<main class="stage">

  <section class="card card-front" aria-label="Business card, front">
    <div class="pattern-top" role="img" aria-label="Dark triangular geometric pattern fading down from the top edge"></div>
    <div class="pattern-bottom" role="img" aria-label="Dark triangular geometric pattern rising from the bottom edge"></div>

    <div class="brand">
      <span class="brand-mark"></span>
      <span class="brand-name">Brantley Advisory Group</span>
    </div>

    <div class="contact">
      <h1 class="contact-name">Mark Brantley</h1>
      <hr class="contact-rule">
      <p class="contact-line">
        <svg viewBox="0 0 24 24" aria-hidden="true"><path d="M6.6 10.8a15.2 15.2 0 0 0 6.6 6.6l2.2-2.2a1 1 0 0 1 1-.25 11.4 11.4 0 0 0 3.6.57 1 1 0 0 1 1 1V20a1 1 0 0 1-1 1A17 17 0 0 1 3 4a1 1 0 0 1 1-1h3.5a1 1 0 0 1 1 1c0 1.25.2 2.45.57 3.57a1 1 0 0 1-.25 1z"/></svg>
        425.318.2746
      </p>
      <p class="contact-line">
        <svg viewBox="0 0 24 24" aria-hidden="true"><path d="M2 5h20v14H2z M2 5l10 8 10-8" fill="none" stroke="var(--brand-blue)" stroke-width="2.4"/></svg>
        mbrantley@brantleyag-example.com
      </p>
    </div>
  </section>

  <section class="card card-back" aria-label="Business card, back">
    <div class="pattern-top" role="img" aria-label="Dark triangular geometric pattern fading down from the top edge"></div>
    <div class="pattern-bottom" role="img" aria-label="Dark triangular geometric pattern rising from the bottom edge"></div>

    <div class="brand">
      <span class="brand-mark"></span>
      <span class="brand-name">Brantley Advisory Group</span>
    </div>
  </section>

</main>
</body>
</html>
```